Lumora Assist overview brochure

Take the word document that is attached and turn it into a brochure. (Thinking one page, front and back.) the only existing branding/colors we have is the logo that is on the document. It may require a phone all or a bit of back and forth in text to explain some of the concepts in the attached document.

Target Market(s)

Call centers

Industry/Entity Type

It Service

Font styles to use
Sans Serif

Colors

Designer to choose colors to be used in the design.

Requirements
Must have
• A crisp professional look

```html
<!DOCTYPE html>
<html lang="en">
<head>
<meta charset="utf-8">
<title>Lumora Assist overview brochure</title>
<link href="https://fonts.googleapis.com/css2?family=Source+Sans+3:wght@400;600&display=swap" rel="stylesheet">
<style>
:root{
  --blue:#27a8e0;
  --blue-soft:#9fd6ea;
  --blue-band:#7cc3d9;
  --grey-dark:#58595b;
  --grey-mid:#8a8b8d;
  --grey-panel:#efefef;
  --text:#4a4a4c;
  --stage:#e4e1dc;
}
*{box-sizing:border-box;margin:0;padding:0}
html,body{width:1200px;height:857px;overflow:hidden;background:var(--stage);font-family:"Source Sans 3",sans-serif;color:var(--text)}
.page{position:absolute;width:498px;height:644px;background:#fff;overflow:hidden;box-shadow:0 4px 14px rgba(0,0,0,.18)}
.page--front{left:74px;top:56px}
.page--back{left:629px;top:130px}
.shapes{position:absolute;left:0;top:0}
.brand{position:absolute;display:flex;align-items:center;gap:7px;color:var(--blue);font-weight:600;letter-spacing:.5px;text-transform:uppercase}
.brand__dot{width:26px;height:26px;border-radius:50%;background:var(--blue)}
.page--back .brand{color:#fff}
.page--back .brand__dot{background:#fff;width:22px;height:22px}
.headline{position:absolute;left:14px;right:14px;top:304px;text-align:center;color:var(--blue);font-size:13px;line-height:16px;font-weight:400;white-space:nowrap;z-index:1}
.body-copy{position:absolute;left:22px;width:273px;top:355px;font-size:8.8px;line-height:10.9px;text-align:justify}
.body-copy p{margin-bottom:5px}
.cost-box{position:absolute;left:323px;top:378px;width:145px;height:182px;background:var(--blue-soft);padding:42px 10px 0}
.cost-box::after{content:"";position:absolute;left:0;right:0;bottom:0;height:10px;background:var(--blue-band)}
.cost-box__arrow{position:absolute;left:385px;top:560px;width:0;height:0;border-left:11px solid transparent;border-right:11px solid transparent;border-top:11px solid var(--blue-band)}
.cost-box__badge{position:absolute;left:368px;top:352px;width:54px;height:54px;border-radius:50%;background:#c9e9f4;display:flex;align-items:center;justify-content:center}
.cost-box__badge span{width:40px;height:40px;border-radius:50%;background:#fff;display:flex;align-items:center;justify-content:center}
.cost-box__title{text-align:center;font-size:10.2px;font-weight:400;letter-spacing:.6px;line-height:16px;color:var(--grey-dark);padding-bottom:4px;border-bottom:1px solid #fff;margin-bottom:10px}
.cost-box ul{list-style:none;font-size:9.6px;line-height:12px;color:var(--grey-dark)}
.cost-box li{display:flex;gap:6px;margin-bottom:9px}
.contact{position:absolute;font-size:10px;line-height:15px;color:#fff}
.contact li{list-style:none;display:flex;align-items:center;gap:6px}
.contact--front{right:18px;top:596px;text-align:right}
.contact--front li{justify-content:flex-end}
.contact--back{left:16px;top:594px}
.contact__icon{width:10px;height:10px;background:var(--blue);border-radius:2px;display:inline-block}
.photo{position:absolute}
.callout{position:absolute;left:15px;top:185px;width:214px;height:116px;background:var(--blue-soft);padding:9px 10px 0;text-align:center;font-size:9.5px;line-height:12.5px;color:var(--grey-dark)}
.callout p{margin-bottom:7px}
.callout::after{content:"";position:absolute;left:0;right:0;bottom:0;height:9px;background:var(--blue-band)}
.panel{position:absolute;left:0;top:207px;width:236px;height:437px;background:var(--grey-panel)}
.channels{position:absolute;left:58px;top:330px;width:130px;display:grid;grid-template-columns:repeat(4,28px);gap:6px 6px}
.channel{display:flex;flex-direction:column;align-items:center;gap:1px;font-size:5px;color:var(--grey-mid);white-space:nowrap}
.channel i{display:block;width:23px;height:23px;border-radius:5px}
.caption{position:absolute;left:18px;width:210px;top:403px;text-align:center;font-size:9.2px;line-height:11.4px}
.model-band{position:absolute;left:0;top:454px;width:240px;height:22px;background:var(--blue-band);color:var(--grey-dark);font-size:11.5px;letter-spacing:.3px;padding:3px 16px}
.section-title{color:var(--blue);font-size:9.6px;font-weight:400;margin-bottom:2px;text-transform:uppercase}
.proposal{position:absolute;left:16px;width:212px;top:496px;font-size:9.2px;line-height:11.4px}
.details{position:absolute;left:260px;width:226px;top:226px;font-size:8.9px;line-height:11.4px}
.details ul{list-style:none;margin:2px 0 12px}
.details li::before{content:"• "}
</style>
</head>
<body>

<section class="page page--front" aria-label="Brochure front">
  <div class="photo" role="img" aria-label="Photo of a smiling call center agent wearing a headset, colleagues blurred behind" style="left:0;top:0;width:498px;height:283px;background:linear-gradient(100deg,#f4f3f2 0%,#e6ddd6 35%,#d8c3b3 60%,#efe9e4 100%)"></div>
  <svg class="shapes" width="498" height="644" viewBox="0 0 498 644">
    <polygon points="0,212 340,283 0,283" fill="#6d6e70" opacity=".85"/>
    <polygon points="0,262 200,283 0,283" fill="var(--grey-dark)"/>
    <polygon points="250,283 498,187 498,320" fill="var(--blue)"/>
    <polygon points="0,587 280,644 0,644" fill="var(--blue)"/>
    <polygon points="230,644 498,570 498,644" fill="var(--grey-dark)"/>
  </svg>
  <div class="brand" style="left:30px;top:60px;font-size:21px;line-height:21px"><span class="brand__dot"></span>Lumora Assist</div>

  <h1 class="headline">Lumora Assist helps contact centers serve new customer<br>access channels, improve customer service, and lower costs of operation.</h1>

  <div class="body-copy">
    <p>The huge popularity of social media and messaging is creating customer preferences to communicate with your company using SMS text messaging, Relay Messenger, Huddlr, Vesta, Nimbra Voice, Homenest, and many other new channels.</p>
    <p>App fatigue has set in. Customers are weary of installing, updating and learning how to use mobile apps. Your customers want to communicate with you using their messaging service of choice or just talk into their smart phone, computer, Nimbra Voice or similar device.</p>
    <p>Sensible automation of customer interactions on these new channels can provide better service at even lower costs of operation.</p>
    <p>According to Calder Research's report, by 2020, 85% of customer interactions will be managed without a human.</p>
    <p>Using specific techniques, Lumora Assist will help you shift some traffic from higher cost telephone calls to lower cost messaging channels. Shaping your traffic into lower cost channels has great financial benefits.</p>
  </div>

  <div class="cost-box">
    <h2 class="cost-box__title">EXISTING CHANNELS<br>HAVE DIFFERENT COSTS</h2>
    <ul>
      <li><svg width="11" height="11" viewBox="0 0 11 11"><rect x=".5" y="1.5" width="8" height="8" fill="none" stroke="#58595b"/><path d="M2.5 5l2 2 5-6" fill="none" stroke="#58595b" stroke-width="1.3"/></svg><span>Telephone call with<br>a live agent</span></li>
      <li><svg width="11" height="11" viewBox="0 0 11 11"><rect x=".5" y="1.5" width="8" height="8" fill="none" stroke="#58595b"/><path d="M2.5 5l2 2 5-6" fill="none" stroke="#58595b" stroke-width="1.3"/></svg><span>Webchat with a<br>live agent</span></li>
    </ul>
  </div>
  <div class="cost-box__arrow"></div>
  <div class="cost-box__badge"><span><svg width="20" height="16" viewBox="0 0 20 16"><path d="M2 1h13a1 1 0 0 1 1 1v8a1 1 0 0 1-1 1H7l-4 4v-4H2a1 1 0 0 1-1-1V2a1 1 0 0 1 1-1z" fill="var(--grey-dark)"/></svg></span></div>

  <ul class="contact contact--front">
    <li>0000 0000 <span class="contact__icon"></span></li>
    <li>lumoraassist@com <span class="contact__icon"></span></li>
    <li>www.lumoraassist.com <span class="contact__icon"></span></li>
  </ul>
</section>

<section class="page page--back" aria-label="Brochure back">
  <div class="photo" role="img" aria-label="Photo of a smiling man reading his phone against warm city lights" style="left:0;top:0;width:498px;height:207px;background:linear-gradient(100deg,#7a6d66 0%,#a89585 40%,#5d4f48 70%,#cfc3b8 100%)"></div>
  <svg class="shapes" width="498" height="644" viewBox="0 0 498 644">
    <polygon points="0,0 258,0 0,122" fill="var(--blue)"/>
    <polygon points="0,122 120,65 90,122" fill="#1e8fc2" opacity=".7"/>
  </svg>
  <div class="panel"></div>
  <svg class="shapes" width="498" height="644" viewBox="0 0 498 644">
    <polygon points="0,549 390,644 0,644" fill="var(--grey-dark)"/>
    <polygon points="498,569 226,644 498,644" fill="var(--blue)"/>
  </svg>
  <div class="brand" style="left:18px;top:32px;font-size:16px;line-height:16px"><span class="brand__dot"></span>Lumora Assist</div>

  <div class="callout">
    <p>Can we create a visual effect that makes it look like a portion of the above is being moved/channeled/shaped to the below?</p>
    <p>Maybe something like a funnel siphoning off some of the above to the below.</p>
    <p>Or a river diverting some of the stream?</p>
  </div>

  <div class="channels">
    <div class="channel"><i style="background:#2b7fc4"></i>Nimbra</div>
    <div class="channel"><i style="background:#3fbf4f"></i>TalkLoop</div>
    <div class="channel"><i style="background:#2fb55a"></i>ChatWave</div>
    <div class="channel"><i style="background:#e8f3d8"></i>Pingly</div>
    <div class="channel"><i style="background:#3c8ee6;border-radius:50%"></i>Relay</div>
    <div class="channel"><i style="background:#d9dadb;border-radius:50%"></i>SMS</div>
    <div class="channel"><i style="background:#c7c0d6"></i>Huddlr</div>
    <div class="channel"><i style="background:#f0d3c9"></i>Homenest</div>
  </div>

  <p class="caption">With these new channels, the cost is similar to webchat. Carefully automated interactions are at an even lower cost.</p>

  <div class="model-band">ENGAGEMENT MODEL</div>

  <div class="proposal">
    <h3 class="section-title">Proposal</h3>
    <p>Lumora Assist provides a written proposal. The proposal will describe our engagement methodologies and costs.</p>
  </div>

  <div class="details">
    <h3 class="section-title">Engagement</h3>
    <p>Lumora Assist will meet with all the relevant stake holders on site and gather information to identify:</p>
    <ul>
      <li>Historical traffic patterns</li>
      <li>Actual costs by channel</li>
      <li>Review marketing plans that may impact customer service</li>
      <li>Review product plans that may impact customer service.</li>
      <li>Explore competition landscape as it relates to customer service.</li>
      <li>Review the existing corporate data store, analytics and reporting</li>
      <li>Review the current plans, metrics and budgets for customer service support</li>
    </ul>
    <h3 class="section-title">Transformation Report</h3>
    <ul>
      <li>Executive summary</li>
      <li>Cost analysis per contact by channel</li>
      <li>Traffic patterns by channel</li>
      <li>Probable impacts of product and marketing plans</li>
      <li>Recommendations for achieving competitive advantage through service</li>
      <li>Recommendations for new channel types</li>
      <li>Recommendations for traffic shaping</li>
      <li>Near and long-term options for sensible automation</li>
      <li>Technology recommendations for implementing new channels</li>
      <li>Projected financial impact of recommendations</li>
    </ul>
  </div>

  <ul class="contact contact--back">
    <li><span class="contact__icon"></span> 0000 0000</li>
    <li><span class="contact__icon"></span> lumoraassist@com</li>
    <li><span class="contact__icon"></span> www.lumoraassist.com</li>
  </ul>
</section>

</body>
</html>
```